Bottle label design for a mulberry brandy

Please create a label design for a mulberry brandy. The registered brand name is "Kolvat"
The brandy will be produced in Armenia from 100% mulberry.
Color of the product: transparent.
The product will be sold worldwide. The price will be between 30 and 50 USD. So the product will be in premium category.
Therefore we need a solid design, appropriate to the product price category. The design, however, needs to be modern and optimistic.
You can have mulberries on the label or not have, it is up to you.
We have chosen for the product some bottle types, the links to the available bottles you can find in the attachment. Ideally you show a picture of your label on the bottle you selected.

Target Market(s)

worldwide

```html
<!DOCTYPE html>
<html lang="en">
<head>
<meta charset="utf-8">
<title>Kolvat Mulberry Brandy – Label</title>
<link rel="stylesheet" href="https://fonts.googleapis.com/css2?family=IBM+Plex+Sans:wght@400;600&display=swap">
<style>
  :root {
    --page: #ffffff;
    --label: #1c1c1c;
    --accent: #0fb0dc;
  }
  * { margin: 0; padding: 0; box-sizing: border-box; }
  html, body {
    width: 927px;
    height: 1200px;
    overflow: hidden;
    background: var(--page);
  }
  .canvas {
    position: relative;
    width: 927px;
    height: 1200px;
  }
  .label {
    position: absolute;
    left: 117px;
    top: 60px;
    width: 693px;
    height: 1080px;
    background: var(--label);
    color: var(--accent);
    font-family: "IBM Plex Sans", sans-serif;
    font-weight: 400;
  }
  .brand-name {
    position: absolute;
    left: 146px;
    top: 210px;
    font-weight: 400;
    font-size: 60px;
    line-height: 1;
    letter-spacing: 0.02em;
  }
  .content-claim {
    position: absolute;
    left: 116px;
    top: 500px;
    font-size: 27px;
    font-weight: 400;
    letter-spacing: 0.06em;
  }
  .product-type {
    position: absolute;
    left: 361px;
    top: 700px;
    font-size: 48px;
    font-weight: 400;
    line-height: 54px;
    letter-spacing: 0.06em;
  }
  .origin {
    position: absolute;
    left: 359px;
    top: 896px;
    font-size: 24px;
    line-height: 28px;
    letter-spacing: 0.04em;
  }
  .volume {
    position: absolute;
    left: 359px;
    top: 1008px;
    font-size: 27px;
  }
</style>
</head>
<body>
<main class="canvas">
  <section class="label">
    <h1 class="brand-name">Kolvat</h1>
    <p class="content-claim">100% MULBERRY</p>
    <h2 class="product-type">MULBERRY<br>BRANDY</h2>
    <p class="origin">PRODUCED<br>IN ARMENIA</p>
    <p class="volume">Vol% 40 500ml</p>
  </section>
</main>
</body>
</html>
```